Brochure Design for Reedmoor.com.au

Local print 'What's On' guide for Reedmoor QLD, Australia. This is basically an entertainment guide listing live music from local pubs, clubs restaurants. Also stories on local events, markets festivals etc. This is a bayside location.

```html
<!DOCTYPE html>
<html lang="en">
<head>
<meta charset="utf-8">
<title>Reedmoor – What's On</title>
<link rel="stylesheet" href="https://fonts.googleapis.com/css2?family=Tinos:ital,wght@0,400;0,700;1,400&family=Source+Sans+3:wght@400&display=swap">
<style>
  :root {
    --bay-blue: #17b2e9;
    --ink-blue: #1a9fd8;
    --date-strip: #d5edf8;
    --sand: #fdf6e6;
    --paper: #ffffff;
    --body-ink: #4a4a4a;
    --rule: #9fd7ef;
    --sky: #aebfcc;
    --water: #5f7f95;
  }
  html, body {
    margin: 0;
    padding: 0;
    overflow: hidden;
    background: var(--paper);
  }
  .guide {
    position: relative;
    width: 846px;
    height: 1200px;
    overflow: hidden;
    background: var(--paper);
    font-family: "Source Sans 3", Arial, sans-serif;
    color: var(--body-ink);
  }
  .masthead {
    position: absolute;
    left: 0; top: 0;
    width: 846px; height: 247px;
    background: var(--bay-blue);
    color: var(--paper);
    font-family: "Tinos", "Times New Roman", serif;
  }
  .masthead__suburbs {
    position: absolute;
    left: 0; right: 0; top: 48px;
    text-align: center;
    font-size: 28px;
    letter-spacing: 0.3px;
    margin: 0;
  }
  .masthead__rule {
    position: absolute;
    left: 64px; right: 64px; top: 96px;
    height: 1px;
    background: rgba(255,255,255,0.45);
  }
  .masthead__title {
    position: absolute;
    left: 0; right: 0; top: 96px;
    margin: 0;
    text-align: center;
    font-weight: 400;
    font-size: 142px;
    line-height: 140px;
    letter-spacing: 2px;
  }
  .dateline {
    position: absolute;
    top: 247px; height: 36px;
    font-family: "Tinos", "Times New Roman", serif;
    font-style: italic;
    font-size: 17px;
    line-height: 36px;
    color: #222;
  }
  .dateline--site { left: 0; width: 527px; padding-left: 64px; box-sizing: border-box; background: var(--paper); }
  .dateline--date { left: 527px; width: 319px; background: var(--date-strip); text-align: right; padding-right: 66px; box-sizing: border-box; }
  .listings-panel {
    position: absolute;
    left: 527px; top: 283px;
    width: 319px; height: 917px;
    background: var(--sand);
  }
  .photo {
    position: absolute;
    display: block;
  }
  .photo--kitesurf {
    left: 0; top: 283px; width: 527px; height: 389px;
    background: linear-gradient(180deg, #c9d3dc 0%, var(--sky) 55%, #4f6b5a 66%, var(--water) 72%, #7d98a8 100%);
  }
  .photo--performer {
    left: 551px; top: 345px; width: 233px; height: 166px;
    background: linear-gradient(135deg, #f3d7bf 0%, #b5807a 45%, #5c4a6e 100%);
  }
  .photo--jetty {
    left: 551px; top: 675px; width: 233px; height: 164px;
    background: linear-gradient(180deg, #a9c6dc 0%, #e9d6b8 45%, #6f8ea3 62%, #8a6b4e 100%);
  }
  .feature-band {
    position: absolute;
    left: 0; top: 672px;
    width: 527px; height: 68px;
    background: var(--bay-blue);
  }
  .feature-band__title {
    position: absolute;
    left: 64px; top: 0;
    margin: 0;
    font-family: "Tinos", "Times New Roman", serif;
    font-weight: 700;
    font-size: 41px;
    line-height: 68px;
    color: var(--paper);
  }
  .story {
    position: absolute;
    margin: 0;
    font-size: 15.6px;
    line-height: 23px;
    color: var(--body-ink);
  }
  .story--lead { left: 64px; top: 752px; width: 442px; text-indent: 26px; }
  .section-rule {
    position: absolute;
    left: 64px; top: 876px;
    width: 440px; height: 1px;
    background: var(--rule);
  }
  .section-heading {
    position: absolute;
    margin: 0;
    font-family: "Tinos", "Times New Roman", serif;
    font-weight: 700;
    font-size: 24px;
    color: var(--ink-blue);
    letter-spacing: 0.5px;
  }
  .section-heading--main { left: 64px; top: 896px; }
  .section-heading--side { left: 551px; top: 304px; }
  .story--col1 { left: 64px; top: 936px; width: 220px; text-indent: 26px; }
  .story--col2 { left: 297px; top: 936px; width: 212px; }
  .event-day {
    position: absolute;
    left: 551px;
    margin: 0;
    font-family: "Tinos", "Times New Roman", serif;
    font-weight: 700;
    font-size: 22px;
    color: var(--ink-blue);
  }
  .event-text {
    position: absolute;
    left: 551px; width: 240px;
    margin: 0;
    font-size: 15.6px;
    line-height: 23px;
    color: var(--body-ink);
  }
</style>
</head>
<body>
<main class="guide">
  <header class="masthead">
    <p class="masthead__suburbs">Wat’s on in:&nbsp; Reedmoor • Kelport • Gullcrest • Tarrow</p>
    <div class="masthead__rule"></div>
    <h1 class="masthead__title">REEDMOOR</h1>
  </header>

  <div class="dateline dateline--site">www.reedmoor.com.au</div>
  <div class="dateline dateline--date">29 may 2012</div>

  <aside class="listings-panel"></aside>

  <div class="photo photo--kitesurf" role="img" aria-label="Kitesurfer jumping above the bay water"></div>

  <div class="feature-band">
    <h2 class="feature-band__title">SURF CONTEST</h2>
  </div>
  <p class="story story--lead">Quiant, quis sitetur at underum evenientia nissed mi, ut esti di vidus dolorem nemquo et volupta con con etur, utem nobitati dolorectet voleni ut aut adit odi deliquo coremquidi ulparum ide voluptasimos</p>

  <div class="section-rule"></div>
  <h2 class="section-heading section-heading--main">WAT’S ON:</h2>
  <p class="story story--col1">Quiant, quis sitetur at underum evenientia nissed mi, ut esti di vidus dolorem nemquo et volupta con con etur, utem nobitati dolorectet voleni ut aut adit odi deliquo coremquidi ulparum ide voluptasimos Quiant, quis</p>
  <p class="story story--col2">sitetur at underum evenientia nissed mi, ut esti di vidus dolorem nemquo et volupta con con etur, utem nobitati dolorectet voleni ut aut adit odi deliquo coremquidi ulparum ide voluptasimos</p>

  <h2 class="section-heading section-heading--side">WAT’S ON:</h2>
  <div class="photo photo--performer" role="img" aria-label="Portrait of a featured local singer"></div>
  <h3 class="event-day" style="top:524px">Friday 1</h3>
  <p class="event-text" style="top:551px">Dolorpost exeribus endis etus, soluptur aut verem eate parumet utemostiosa cum ut untur? Quiant, quis sitetur at underum</p>

  <div class="photo photo--jetty" role="img" aria-label="Bayside pier at sunset"></div>
  <h3 class="event-day" style="top:862px">Saturday 2</h3>
  <p class="event-text" style="top:888px">Dolorpost exeribus endis etus, soluptur aut verem eate parumet utemostiosa cum ut untur? Quiant, quis sitetur at underum quis sitetur at</p>

  <h3 class="event-day" style="top:1030px">Sunday 3</h3>
  <p class="event-text" style="top:1056px">Dolorpost exeribus endis etus, soluptur aut verem eate parumet utemostiosa cum ut untur?</p>
</main>
</body>
</html>
```